Online Advertising agency with fun music culture twist

We need a new website for our online advertising agency. The current site is just a placeholder but you can pull the text from the site- pebblebidhouse.com. The new site will be 10 total pages. The current site has 8 pages. So this project will require the design and code for all 10 pages.

Things I like- Clean, easy to read, custom graphics, video,
splash 1-2 colors, futuristic, music twist, fun, interesting, looks amazing on a mobile site, extremely professional design.

Things I don't like- I hate stock graphics, pages that scroll to much, to many colors (rainbow), sites that don't flow, very templated cookie cutter sites, not mobile compliant.

We built a sophisticated buying platform for advertisers to reach the right person on the right device at the right time. I used to be a concert promoter and I have several musicians that work with us. We want to play into the fun and excitement of live music with an advertising twist hence the name Pebble. We don't want to make it seem like a music company but we can use subtle vinyl and music references. My other company is marrowpixel.com for reference. I really like to design of my other company.

Target Market(s)

Online websites and fortune 500 advertisers- You can see my other company at marrowpixel.com

Industry/Entity Type

Advertising

Coding

Coded - Design and coding required

Number of Pages Required

5+ page

Font styles to use
Other font styles liked:
• Be creative

Requirements
Must have
• HTML5, Clean, easy to read, custom graphics, use of video graphics,
• splash 1-2 colors, futuristic, music twist, fun, interesting, looks amazing on a mobile site, extremely professional design. Play into the music theme, vinyl records etc
Nice to have
• Video, interactivity, custom build (not a template)
Should not have
• Flash. I hate stock photos, pages that scroll to much, to many colors (rainbow), sites that don't flow, very templated cookie cutter sites, not mobile compliant.

```html
<!DOCTYPE html>
<html lang="en">
<head>
<meta charset="utf-8">
<title>Pebble Trading Desk</title>
<link href="https://fonts.googleapis.com/css2?family=Montserrat:wght@400;500;600;700&family=Open+Sans:wght@400;600&display=swap" rel="stylesheet">
<style>
:root{
  --ink:#1d1d1d;
  --body:#555;
  --muted:#888;
  --orange:#e9962e;
  --orange-dark:#d9862a;
  --teal:#2aa7cf;
  --hero-b:#151515;
  --soft:#f1f1f1;
  --footer:#efefef;
  --line:#dcdcdc;
  --white:#fff;
}
*{margin:0;padding:0;box-sizing:border-box}
html,body{width:1200px;height:2703px;overflow:hidden;background:var(--white)}
body{font-family:"Open Sans",sans-serif;color:var(--body);position:relative}
.heading{font-family:"Montserrat",sans-serif;color:var(--ink);font-weight:700;text-transform:uppercase}

/* hero */
.hero{position:absolute;left:0;top:0;width:1200px;height:627px;background:radial-gradient(ellipse at 60% 40%,#3a3a3a,var(--hero-b) 75%);overflow:hidden}
.equalizer{position:absolute;left:0;bottom:0;opacity:.14}
.brand{position:absolute;left:88px;top:22px;color:var(--white);font-family:"Montserrat",sans-serif}
.brand-name{font-size:38px;font-weight:600;letter-spacing:3px;line-height:1}
.brand-sub{font-size:13px;letter-spacing:4px;text-align:center;border-top:1px solid #999;margin-top:4px;padding-top:2px;color:#ccc}
.nav{position:absolute;right:88px;top:36px;display:flex;gap:45px;font-family:"Montserrat",sans-serif;font-size:14px;color:var(--white)}
.hero-title{position:absolute;top:228px;width:100%;text-align:center;color:var(--white);font-family:"Montserrat",sans-serif;font-weight:700;font-size:47px;letter-spacing:1px}
.hero-sub{position:absolute;top:296px;width:100%;text-align:center;color:#eee;font-family:"Montserrat",sans-serif;font-size:24px}
.btn-outline{position:absolute;border:1px solid #ddd;color:var(--white);font-family:"Montserrat",sans-serif;display:flex;align-items:center;justify-content:center}
.hero .btn-outline{left:481px;top:377px;width:238px;height:45px;font-size:16px}
.arrow{position:absolute;top:275px}

/* welcome */
.welcome-title{position:absolute;left:88px;top:692px;font-size:26px}
.welcome-text{position:absolute;left:88px;top:745px;width:524px;font-size:11.5px;line-height:22px;text-align:justify}
.welcome-text p{margin-bottom:14px}
.btn-solid{position:absolute;left:88px;top:912px;width:159px;height:41px;background:var(--orange);color:var(--white);font-family:"Montserrat",sans-serif;font-size:13px;font-weight:600;display:flex;align-items:center;padding-left:16px}
.btn-solid span{position:absolute;right:0;top:0;width:46px;height:41px;border-left:1px solid rgba(255,255,255,.4);display:flex;align-items:center;justify-content:center}
.laptop-shot{position:absolute;left:663px;top:690px;width:449px;height:278px;background:linear-gradient(#e3e3e3,#c9c9c9);border-radius:10px}

/* services */
.services{position:absolute;left:0;top:1031px;width:1200px;height:437px;background:var(--soft);overflow:hidden}
.section-title{position:absolute;width:100%;text-align:center;font-size:24px}
.services .section-title{top:56px}
.grooves{position:absolute;left:0;top:0}
.service{position:absolute;width:280px}
.service h3{font-family:"Montserrat",sans-serif;font-size:16px;font-weight:600;color:var(--ink);margin-bottom:10px}
.service p{font-size:11.5px;line-height:24px}
.service.left{text-align:right}
.service-icon{position:absolute}
.mark{position:absolute;left:500px;top:1162px;width:200px;height:240px;display:flex;flex-direction:column;align-items:center;justify-content:center;gap:14px;font-family:"Montserrat",sans-serif;font-size:32px;font-weight:700;color:var(--teal);letter-spacing:3px}
.mark i{width:120px;height:120px;border-radius:50%;background:var(--teal);display:block}

/* scale band */
.scale{position:absolute;left:0;top:1468px;width:1200px;height:334px;background:linear-gradient(100deg,var(--orange),var(--orange-dark));overflow:hidden}
.wave{position:absolute;left:0;top:0;opacity:.22}
.scale-title{position:absolute;top:70px;width:100%;text-align:center;color:var(--white);font-family:"Montserrat",sans-serif;font-size:32px;font-weight:600}
.scale-text{position:absolute;top:128px;left:210px;width:780px;text-align:center;color:#fff3e2;font-size:16px;line-height:29px}
.scale .btn-outline{left:510px;top:217px;width:169px;height:41px;font-size:13px;border-color:#fff3e2}

/* blog */
.blog .section-title{top:1856px}
.post{position:absolute;top:1919px;width:321px}
.post-image{width:321px;height:184px}
.post h4{font-family:"Montserrat",sans-serif;font-size:15px;font-weight:600;color:var(--ink);margin-top:24px}
.post-meta{font-size:8px;color:var(--muted);margin-top:6px;letter-spacing:.5px}
.post p{font-size:11.5px;line-height:24px;margin-top:10px}

/* partners */
.partners{position:absolute;top:2262px;left:88px;width:1024px;height:80px;display:flex;justify-content:space-between;align-items:center;font-family:"Open Sans",sans-serif;font-weight:600;font-size:26px;color:#333}
.partners .badge{display:flex;align-items:center;gap:10px}
.partners .dot{width:22px;height:22px;border-radius:50%;background:#333}
.partners .sq{width:22px;height:22px;background:#333}

/* footer */
.footer{position:absolute;left:0;top:2387px;width:1200px;height:316px;background:var(--footer)}
.footer-col{position:absolute;top:52px}
.footer-col h5{font-family:"Montserrat",sans-serif;font-size:16px;font-weight:600;color:var(--ink);margin-bottom:12px}
.footer-col li{list-style:none;font-size:12px;line-height:26px}
.signup{font-size:12px;margin-bottom:12px}
.mail{width:256px;height:36px;border:1px solid var(--line);background:var(--white);display:flex;align-items:center;font-size:10px;color:#aaa;font-style:italic;padding-left:14px;position:relative}
.mail span{position:absolute;right:0;top:0;width:44px;height:34px;border-left:1px solid var(--line);display:flex;align-items:center;justify-content:center;background:#e6e6e6}
.footer-rule{position:absolute;left:88px;top:246px;width:1024px;border-top:1px solid var(--line)}
.copyright{position:absolute;top:272px;width:100%;text-align:center;font-size:12px}
</style>
</head>
<body>

<header class="hero">
  <svg class="equalizer" width="1200" height="170" viewBox="0 0 1200 170" aria-hidden="true">
    <g fill="#fff">
      <rect x="20" y="110" width="14" height="60"/><rect x="44" y="80" width="14" height="90"/><rect x="68" y="120" width="14" height="50"/><rect x="92" y="60" width="14" height="110"/><rect x="116" y="95" width="14" height="75"/><rect x="140" y="130" width="14" height="40"/><rect x="164" y="70" width="14" height="100"/><rect x="188" y="105" width="14" height="65"/><rect x="212" y="125" width="14" height="45"/><rect x="236" y="85" width="14" height="85"/>
      <rect x="950" y="100" width="14" height="70"/><rect x="974" y="70" width="14" height="100"/><rect x="998" y="120" width="14" height="50"/><rect x="1022" y="55" width="14" height="115"/><rect x="1046" y="90" width="14" height="80"/><rect x="1070" y="125" width="14" height="45"/><rect x="1094" y="75" width="14" height="95"/><rect x="1118" y="110" width="14" height="60"/><rect x="1142" y="95" width="14" height="75"/><rect x="1166" y="130" width="14" height="40"/>
    </g>
  </svg>
  <div class="brand"><div class="brand-name">PEBBLE</div><div class="brand-sub">Trading Desk</div></div>
  <nav class="nav"><span>HOME</span><span>ABOUT US</span><span>ADVERTISERS</span><span>PUBLISHERS</span><span>CONTACT US</span></nav>
  <svg class="arrow" style="left:32px" width="30" height="70" viewBox="0 0 30 70"><polyline points="28,2 2,35 28,68" fill="none" stroke="#aaa" stroke-width="2"/></svg>
  <svg class="arrow" style="right:32px" width="30" height="70" viewBox="0 0 30 70"><polyline points="2,2 28,35 2,68" fill="none" stroke="#aaa" stroke-width="2"/></svg>
  <h1 class="hero-title">PEBBLE TRADING DESK</h1>
  <p class="hero-sub">Your Advertising Made Easy With A Unified Buying Platform</p>
  <div class="btn-outline">GET IN TOUCH WITH US</div>
</header>

<section class="welcome">
  <h2 class="heading welcome-title">Welcome to Pebble Trading Desk</h2>
  <div class="welcome-text">
    <p>Pebble Trading Desk Is A Global Digital Media Platform That Programmatically Connects Advertisers And Publishers To Audiences Across All Addressable Channels. Our Technology And Services Enable Marketers To Reach The Audiences They Want At The Scale They Need To Achieve</p>
    <p>Today, advertisers want to measure brand engagement. Campaign goals and objectives are defined by it. Pebble's system of sophisticated, customized and targeted media placement</p>
  </div>
  <div class="btn-solid">LEARN MORE <span>»</span></div>
  <div class="laptop-shot" role="img" aria-label="Laptop showing the Pebble Trading Desk name on screen"></div>
</section>

<section class="services">
  <svg class="grooves" width="1200" height="437" viewBox="0 0 1200 437" aria-hidden="true">
    <g fill="none" stroke="#e4e4e4" stroke-width="1.5">
      <circle cx="600" cy="250" r="150"/><circle cx="600" cy="250" r="175"/><circle cx="600" cy="250" r="200"/><circle cx="600" cy="250" r="225"/>
    </g>
  </svg>
  <h2 class="heading section-title">Our Services</h2>
</section>
<div class="service left" style="left:80px;top:1187px"><h3>CROSS-CHANNEL TARGETING</h3><p>We'll help you reach viewers across devicestho the through video, display, mobile and native</p></div>
<svg class="service-icon" style="left:375px;top:1188px" width="36" height="30" viewBox="0 0 36 30"><rect x="8" y="2" width="26" height="18" fill="none" stroke="#444" stroke-width="2"/><rect x="2" y="8" width="10" height="18" fill="#fff" stroke="#444" stroke-width="2"/><line x1="16" y1="26" x2="28" y2="26" stroke="#444" stroke-width="2"/></svg>
<div class="service left" style="left:80px;top:1296px"><h3>AUTOMATED BUYING</h3><p>Our unified programmaticmarketplace provides efficiency and drivesmaximum return spend.</p></div>
<svg class="service-icon" style="left:420px;top:1300px" width="52" height="44" viewBox="0 0 52 44"><g fill="none" stroke="#444" stroke-width="3"><circle cx="18" cy="18" r="9"/><circle cx="38" cy="32" r="6"/></g><g stroke="#444" stroke-width="4"><line x1="18" y1="3" x2="18" y2="33"/><line x1="3" y1="18" x2="33" y2="18"/><line x1="38" y1="23" x2="38" y2="41"/><line x1="29" y1="32" x2="47" y2="32"/></g><circle cx="18" cy="18" r="5" fill="#f1f1f1"/><circle cx="38" cy="32" r="3" fill="#f1f1f1"/></svg>
<div class="mark" role="img" aria-label="Pebble brand mark"><i></i>PEBBLE</div>
<svg class="service-icon" style="left:766px;top:1188px" width="26" height="34" viewBox="0 0 26 34"><rect x="2" y="2" width="20" height="28" fill="none" stroke="#444" stroke-width="2"/><g stroke="#444" stroke-width="2"><line x1="6" y1="9" x2="18" y2="9"/><line x1="6" y1="14" x2="12" y2="14"/></g><circle cx="17" cy="23" r="6" fill="#444"/></svg>
<div class="service" style="left:809px;top:1187px"><h3>FULL TRANSPARENCY</h3><p>We think you should know and control the media you're paying for. Don't you?</p></div>
<svg class="service-icon" style="left:718px;top:1300px" width="50" height="30" viewBox="0 0 50 30"><path d="M2 10 L14 4 L26 10 L36 4 L48 10 L44 18 L30 28 L20 22 L6 18 Z" fill="#444"/></svg>
<div class="service" style="left:780px;top:1296px"><h3>TRUE PARTNERSHIPS</h3><p>ur goal is to build long-lasting relationships in business and in life.</p></div>

<section class="scale">
  <svg class="wave" width="1200" height="334" viewBox="0 0 1200 334" aria-hidden="true">
    <g fill="none" stroke="#fff" stroke-width="2">
      <path d="M0 300 C100 260 200 330 300 295 S500 255 600 295 S800 335 900 295 S1100 255 1200 295"/>
      <path d="M0 40 C100 10 200 70 300 40 S500 10 600 40 S800 70 900 40 S1100 10 1200 40"/>
    </g>
  </svg>
  <h2 class="scale-title">GLOBAL SCALE WITH ROI TOP OF MIND</h2>
  <p class="scale-text">Our technology and services enable marketers to connect with the audiences they want at the scale they need to achieve the outcomes they desire.</p>
  <div class="btn-outline">VIEW CASE STUDIES</div>
</section>

<section class="blog">
  <h2 class="heading section-title">Our Recent Blog Post</h2>
  <article class="post" style="left:90px"><div class="post-image" role="img" aria-label="Hands pointing at a laptop on a desk" style="background:linear-gradient(135deg,#d9dde1,#8d8f92)"></div><h4>MAXIME PLACEAT FACERE</h4><div class="post-meta">AUGUST 2, 2016 &nbsp;|&nbsp; 1 COMMENT(S)</div><p>It is a long established fact that a reader will be distracted by the readable content of a page when looking...</p></article>
  <article class="post" style="left:441px"><div class="post-image" role="img" aria-label="Desk with charts, calculator and laptop" style="background:linear-gradient(135deg,#b9b3a8,#6e6a63)"></div><h4>MAXIME PLACEAT FACERE</h4><div class="post-meta">AUGUST 2, 2016 &nbsp;|&nbsp; 1 COMMENT(S)</div><p>It is a long established fact that a reader will be distracted by the readable content of a page when looking...</p></article>
  <article class="post" style="left:791px"><div class="post-image" role="img" aria-label="Stacks of coins in front of a market board" style="background:linear-gradient(160deg,#2b2420,#8a5a30 70%,#5a3a22)"></div><h4>MAXIME PLACEAT FACERE</h4><div class="post-meta">AUGUST 2, 2016 &nbsp;|&nbsp; 1 COMMENT(S)</div><p>It is a long established fact that a reader will be distracted by the readable content of a page when looking...</p></article>
</section>

<div class="partners">
  <span class="badge">Marlo's<i class="dot"></i></span>
  <span>Kiln&amp;Cove</span>
  <span>Rivet Co</span>
  <span class="badge"><i class="dot"></i>Fairleaf</span>
  <span class="badge"><i class="sq"></i>Northpine Lending</span>
</div>

<footer class="footer">
  <div class="footer-col" style="left:88px"><h5>COMPANY</h5><ul><li>Home</li><li>Advertisers</li><li>Publishers</li><li>About Us</li></ul></div>
  <div class="footer-col" style="left:301px"><h5>PEBBLE DIFFERENCE</h5><ul><li>Simplicity</li><li>Accountability at Scale.</li><li>Transparent media buying</li><li>Streamline your supply chain.</li></ul></div>
  <div class="footer-col" style="left:587px"><h5>WHY US</h5><ul><li>Unified Buying &amp; Reporting</li><li>Automated Media Buying</li><li>Improved Ad Targeting</li><li>Partners</li></ul></div>
  <div class="footer-col" style="left:856px"><h5>NEWSLETTER</h5><p class="signup">SIGN UP FOR A FREE WEEK!</p><div class="mail">Enter Your Mail Id<span><svg width="14" height="14" viewBox="0 0 14 14"><path d="M1 7 L13 1 L9 13 L7 8 Z" fill="#444"/></svg></span></div></div>
  <div class="footer-rule"></div>
  <p class="copyright">Copyrights@CompanyName , All rights Reserved</p>
</footer>

</body>
</html>
```